Business card and stationary for a consultant firm
Sharp Compass
Professional
Renske Hoorneman
Zwaluwlaan 38
Curaçao
Renskehoorneman@postvlek.com
Zwaluwlaan38

```html
<!DOCTYPE html>
<html lang="en">
<head>
<meta charset="utf-8">
<title>Sharp Compass — Business Card</title>
<link rel="stylesheet" href="https://fonts.googleapis.com/css2?family=Cormorant+Garamond:wght@600&family=Cormorant+SC:wght@500;600&display=swap">
<style>
  :root {
    --backdrop: #e9e6e1;
    --card: #ffffff;
    --ink: #1c1c1c;
    --text-grey: #5a5a5a;
    --accent-orange: #e07a1e;
    --olive: #a39a22;
    --olive-soft: #b8ae3c;
    --corner-dark: #2a2a22;
  }
  * { margin: 0; padding: 0; box-sizing: border-box; }
  html, body {
    width: 1200px; height: 914px; overflow: hidden;
    background: var(--backdrop);
  }
  .business-card {
    position: absolute; left: 50px; top: 142px;
    width: 1100px; height: 629px;
    background: var(--card);
    box-shadow: 0 6px 24px rgba(0,0,0,0.12);
    overflow: hidden;
  }
  .corner-area { position: absolute; inset: 0; width: 1100px; height: 629px; }
  .brand {
    position: absolute; left: 70px; top: 78px;
    display: flex; align-items: center; gap: 28px;
  }
  .brand-mark {
    width: 96px; height: 96px; border-radius: 50%;
    background: var(--olive);
  }
  .brand-name {
    font-family: "Cormorant Garamond", serif;
    font-weight: 600; font-size: 60px; color: var(--ink);
    letter-spacing: 0.5px; line-height: 1;
  }
  .contact-list {
    position: absolute; left: 70px; top: 292px;
    list-style: none;
    font-family: "Cormorant SC", serif; font-weight: 500;
    font-size: 25px; color: var(--text-grey); letter-spacing: 0.5px;
  }
  .contact-item { display: flex; align-items: center; gap: 16px; height: 36px; }
  .contact-icon { width: 18px; height: 18px; flex: none; }
  .holder-name {
    position: absolute; right: 70px; bottom: 44px;
    font-family: "Cormorant SC", serif; font-weight: 600;
    font-size: 28px; color: var(--accent-orange); letter-spacing: 0.5px;
  }
</style>
</head>
<body>
<div class="business-card">
  <svg class="corner-area" viewBox="0 0 1100 629" role="img" aria-label="Decorative curved corner artwork in black and olive">
    <defs>
      <linearGradient id="corner-fill" x1="0" y1="1" x2="1" y2="0">
        <stop offset="0" stop-color="var(--corner-dark)"/>
        <stop offset="1" stop-color="var(--olive-soft)"/>
      </linearGradient>
    </defs>
    <path d="M640,0 C880,50 1050,250 1100,480 L1100,0 Z" fill="url(#corner-fill)"/>
  </svg>

  <div class="brand">
    <div class="brand-mark"></div>
    <div class="brand-name">Sharpcompass</div>
  </div>

  <ul class="contact-list">
    <li class="contact-item">
      <svg class="contact-icon" viewBox="0 0 18 18"><path d="M2 9 L9 2 L16 9 L14 9 L14 16 L4 16 L4 9 Z" fill="var(--accent-orange)"/></svg>
      Zwaluwlaan 38 Curaçao
    </li>
    <li class="contact-item">
      <svg class="contact-icon" viewBox="0 0 18 18"><rect x="5" y="1" width="8" height="16" rx="1.5" fill="var(--accent-orange)"/><rect x="6.5" y="3" width="5" height="9" fill="var(--card)"/></svg>
      (599 9) 555 0147
    </li>
    <li class="contact-item">
      <svg class="contact-icon" viewBox="0 0 18 18"><rect x="1" y="4" width="16" height="11" fill="var(--accent-orange)"/><path d="M1 4 L9 11 L17 4" fill="none" stroke="var(--card)" stroke-width="1.4"/></svg>
      Renskehoorneman@postvlek.com
    </li>
    <li class="contact-item">
      <svg class="contact-icon" viewBox="0 0 18 18"><circle cx="9" cy="9" r="7.5" fill="none" stroke="var(--accent-orange)" stroke-width="1.6"/><ellipse cx="9" cy="9" rx="3.2" ry="7.5" fill="none" stroke="var(--accent-orange)" stroke-width="1.3"/><line x1="1.5" y1="9" x2="16.5" y2="9" stroke="var(--accent-orange)" stroke-width="1.3"/></svg>
      www.Zwaluwlaan38.com
    </li>
  </ul>

  <div class="holder-name">Renske Hoorneman</div>
</div>
</body>
</html>
```